VorBlend Advantages & Features Advertising

We are VorBlend, a manufacturer offering complete mixing solutions for all industries since 1954. Our engineering & innovation, combined with our performance & quality, value & pricing, backed with the best warranty in the industry has made us the most disruptive brand in the industry.

We need to create an add that promotes our diversity across the Pharmaceutical & Nutraceutical, Food & Beverage, Bakery & Confectionary, Chemical, and Cosmetic / Health & Beauty industries

We need a professional, energetic, and captivating ad the captures the attention of the customer while branding our product.

I have included our logo, along with some png pictures for use.

Our website is www.vorblendco.example and our YouTube channel is you want to find out more about us is https://www.video.example/channel/UCqzTowkL4DMAsYxhaRPiOkb

I have also included our Answers Led Booklet

Please feel free to write if you have any questions

Our engineering & innovation allow us to remain leaders in the industry with our products. Our Merit Built Design allow us to capture the heart of our customers as we include features that allow us to meet the demands of today, while keeping in mind the needs of tomorrow.

Our performance & quality allow us to go head to head with our competition and win while allowing a quick ROI for our customers on their investment

Our value and pricing allow us to meet or exceed our competitors performance & specifications while beating them in price, warranty, and customer service. Exceeding the expectations of customers globally

Target Market(s)

Pharmaceutical & Nutraceutical manufacturers, Food & Beverage manufacturers, Cosmetic & Health/Beauty manufacturers, & Chemical manufacturers

Industry/Entity Type

Manufacturer

Requirements
Must have
• Energy & capture the attention of customer with a focus on branding
Nice to have
• www.vorblendco.example website

```html
<!DOCTYPE html>
<html lang="en">
<head>
<meta charset="utf-8">
<title>VorBlend – Industrial Mixers</title>
<link rel="stylesheet" href="https://fonts.googleapis.com/css2?family=Montserrat:wght@400;500&family=Open+Sans:wght@400;600;700&family=Varela+Round&display=swap">
<style>
  :root {
    --page: #ffffff;
    --ink: #3a3a3a;
    --ink-soft: #555555;
    --muted: #8a8a8a;
    --icon-blue: #2fa6e0;
    --rule: #e3e3e3;
    --hero-light: #f4f4f4;
    --hero-dark: #c9c9c9;
    --tile-1: #37ade0;
    --tile-2: #30b6d2;
    --tile-3: #2dbfc4;
    --tile-4: #2dd0b0;
  }
  * { box-sizing: border-box; margin: 0; padding: 0; }
  html, body { width: 1200px; height: 903px; overflow: hidden; background: var(--page); }
  body { font-family: "Open Sans", sans-serif; color: var(--ink); position: relative; }

  .site-header {
    position: absolute; left: 190px; top: 40px; width: 820px; height: 60px;
    display: flex; align-items: center; justify-content: space-between;
    border-bottom: 1px solid var(--rule);
  }
  .brand-name { font-family: "Varela Round", sans-serif; font-size: 26px; color: var(--ink); line-height: 1; }
  .contact-list { display: flex; gap: 34px; }
  .contact { display: flex; align-items: center; gap: 8px; }
  .contact-icon { width: 26px; height: 26px; border-radius: 50%; background: var(--icon-blue); display: flex; align-items: center; justify-content: center; }
  .contact-label { font-size: 7px; font-weight: 700; color: var(--ink-soft); text-transform: uppercase; }
  .contact-value { font-size: 7.5px; color: var(--muted); }

  .subnav {
    position: absolute; left: 190px; top: 112px; width: 820px;
    display: flex; justify-content: space-between; align-items: center;
  }
  .product-line { font-family: "Montserrat", sans-serif; font-size: 10.5px; letter-spacing: 0.8px; color: var(--ink-soft); }
  .social { display: flex; gap: 12px; }
  .social span { width: 12px; height: 12px; border-radius: 50%; background: var(--ink); display: block; }

  .hero {
    position: absolute; left: 150px; top: 140px; width: 900px; height: 420px;
    background: radial-gradient(ellipse at 35% 30%, var(--hero-light) 0%, #e2e2e2 55%, var(--hero-dark) 100%);
  }
  .hero-copy { position: absolute; left: 60px; top: 105px; width: 400px; text-align: center; }
  .hero-title { font-family: "Open Sans", sans-serif; font-weight: 600; font-size: 27px; line-height: 1.25; color: var(--ink); letter-spacing: -0.5px; }
  .hero-text { margin: 22px auto 0; width: 210px; font-size: 9.5px; line-height: 1.75; color: var(--ink-soft); }
  .hero-gallery { position: absolute; right: 40px; top: 25px; display: flex; gap: 24px; }
  .gallery-panel { width: 104px; height: 390px; }
  .panel-food { background: linear-gradient(180deg, #e9dccf 0%, #d9a98a 30%, #ecebe8 55%, #b8bcc2 80%, #d6d6d6 100%); }
  .panel-lab { background: linear-gradient(180deg, #d8dcef 0%, #9ab0d8 30%, #3b7fc4 45%, #d4d8e0 60%, #9ca2a8 85%, #cfcfcf 100%); }
  .panel-pills { background: linear-gradient(180deg, #f0e7c8 0%, #e4d7e0 25%, #e58aa7 40%, #e4e4e8 60%, #8fa8c4 85%, #d4d4d4 100%); }

  .industries { position: absolute; left: 150px; top: 560px; width: 900px; height: 220px; display: flex; }
  .industry {
    flex: 1; display: flex; flex-direction: column; align-items: center; padding-top: 40px;
    font-family: "Varela Round", sans-serif; color: #ffffff; font-size: 17px; line-height: 1.2; text-align: center;
  }
  .industry:nth-child(1) { background: var(--tile-1); }
  .industry:nth-child(2) { background: var(--tile-2); }
  .industry:nth-child(3) { background: var(--tile-3); }
  .industry:nth-child(4) { background: var(--tile-4); }
  .industry-icon { width: 46px; height: 46px; border-radius: 50%; background: #ffffff; display: flex; align-items: center; justify-content: center; margin-bottom: 28px; }
</style>
</head>
<body>
  <header class="site-header">
    <div class="brand"><span class="brand-name">VorBlend</span></div>
    <div class="contact-list">
      <div class="contact">
        <span class="contact-icon"><svg width="14" height="14" viewBox="0 0 14 14"><circle cx="7" cy="7" r="5.5" fill="none" stroke="#fff" stroke-width="1.4"/><path d="M1.5 7h11M7 1.5c-2.5 3-2.5 8 0 11M7 1.5c2.5 3 2.5 8 0 11" fill="none" stroke="#fff" stroke-width="1"/></svg></span>
        <div><div class="contact-label">Browse us</div><div class="contact-value">www.vorblendco.example</div></div>
      </div>
      <div class="contact">
        <span class="contact-icon"><svg width="14" height="14" viewBox="0 0 14 14"><rect x="1.5" y="3" width="11" height="8" rx="1" fill="#fff"/><path d="M1.5 3.5l5.5 4 5.5-4" fill="none" stroke="#2fa6e0" stroke-width="1"/></svg></span>
        <div><div class="contact-label">Mail us</div><div class="contact-value">dana.k@vorblendco.example</div></div>
      </div>
      <div class="contact">
        <span class="contact-icon"><svg width="14" height="14" viewBox="0 0 14 14"><rect x="4" y="1.5" width="6" height="11" rx="1.2" fill="none" stroke="#fff" stroke-width="1.3"/><circle cx="7" cy="10.5" r="0.7" fill="#fff"/></svg></span>
        <div><div class="contact-label">Call us</div><div class="contact-value">+100 2000 3000</div></div>
      </div>
    </div>
  </header>

  <nav class="subnav">
    <p class="product-line">Power Blenders &amp; Dryers , Paste Kneaders &amp; Mixers , Liquid Dispersers &amp; Mixers.</p>
    <div class="social" aria-label="Social channels">
      <span></span><span></span><span></span><span></span><span></span>
    </div>
  </nav>

  <section class="hero">
    <div class="hero-copy">
      <h1 class="hero-title">Industrial Mixer, Mixing<br>Equipment &amp; Powder Mixers</h1>
      <p class="hero-text">We are VorBlend, a manufacturer offering complete mixing solutions for all industries since 1954. Our engineering &amp; innovation, combined with our performance &amp; quality, value &amp; pricing, backed with the best warranty in the industry has made us the most disruptive brand in the industry.</p>
    </div>
    <div class="hero-gallery">
      <div class="gallery-panel panel-food" role="img" aria-label="Plated food dishes above a stainless steel mixing vessel"></div>
      <div class="gallery-panel panel-lab" role="img" aria-label="Laboratory flask with blue liquid above a stainless steel mixer on a frame"></div>
      <div class="gallery-panel panel-pills" role="img" aria-label="Tablets in blister packs above an inline dispersing pump"></div>
    </div>
  </section>

  <section class="industries">
    <div class="industry">
      <span class="industry-icon"><svg width="26" height="26" viewBox="0 0 26 26" fill="none" stroke="#333" stroke-width="1.5"><rect x="4" y="9" width="12" height="6" rx="3" transform="rotate(-45 10 12)"/><line x1="8" y1="10" x2="12" y2="14"/><circle cx="18" cy="12" r="4"/><line x1="15.5" y1="14.5" x2="20.5" y2="9.5"/></svg></span>
      Pharmaceutical &amp;<br>Nutraceutical<br>manufacturers
    </div>
    <div class="industry">
      <span class="industry-icon"><svg width="26" height="26" viewBox="0 0 26 26" fill="none" stroke="#333" stroke-width="1.4"><circle cx="13" cy="13" r="11"/><circle cx="13" cy="13" r="7"/><path d="M10 8v4M10 12v6M16 8c1.5 1 1.5 4 0 5v5"/></svg></span>
      Food &amp; Beverage<br>manufacturers
    </div>
    <div class="industry">
      <span class="industry-icon"><svg width="26" height="26" viewBox="0 0 26 26" fill="none" stroke="#333" stroke-width="1.5"><rect x="8" y="9" width="10" height="13" rx="2"/><rect x="10.5" y="4" width="5" height="5"/><path d="M13 13.5c-1.5 2-1.5 3.5 0 3.5s1.5-1.5 0-3.5z"/></svg></span>
      Cosmetic &amp; Health<br>Beauty manufacturers
    </div>
    <div class="industry">
      <span class="industry-icon"><svg width="26" height="26" viewBox="0 0 26 26" fill="none" stroke="#333" stroke-width="1.4"><path d="M7 4h5M8.5 4v6l-4 10h11l-4-10V4"/><path d="M6 16h9"/><rect x="17" y="8" width="4" height="14" rx="2"/></svg></span>
      Chemical<br>manufacturers
    </div>
  </section>
</body>
</html>
```